Rainbow card

Looking for someone to design a card using rainbow theme and link 7 different promises of love to each color. The design will be used to either print a greeting card for valentines or flyer type layout to be framed.

Target Market(s)

Personal

Font styles to use
Script

Colors
eb1f27
f78f20
faee3e
9bcb3c
0655a3
6a429a
a64599

Requirements
Must have
• Rainbow
• The phrases to be included on each color are:
• red - I'll never leave you as long as you'll have me.
• orange - I'll never deny you my body.
• yellow - I'll never let you go to prison.
• green - I'll have a baby with you.
• blue - I'll marry you.
• Indigo - I'll always love you.
• Violet - I'll always stand by you and support you.
Nice to have
• Rainbow, love and loyalty significance

```html
<!DOCTYPE html>
<html lang="en">
<head>
<meta charset="utf-8">
<title>Rainbow Promises Card</title>
<link rel="stylesheet" href="https://fonts.googleapis.com/css2?family=Dancing+Script:wght@600&display=swap">
<style>
  :root {
    --paper: #ffffff;
    --ink-light: #ffffff;
    --ink-dark: #5a4a00;
    --red: #eb1f27;
    --orange: #f78f20;
    --yellow: #faee3e;
    --green: #9bcb3c;
    --blue: #0655a3;
    --indigo: #6a429a;
    --violet: #a64599;
  }
  html, body {
    margin: 0;
    padding: 0;
    width: 1200px;
    height: 963px;
    overflow: hidden;
    background: var(--paper);
  }
  .card {
    box-sizing: border-box;
    width: 1200px;
    height: 963px;
    padding: 52px 70px;
    display: flex;
    flex-direction: column;
    gap: 8px;
    background: var(--paper);
    font-family: "Dancing Script", cursive;
  }
  .promise {
    flex: 1;
    margin: 0;
    display: flex;
    align-items: center;
    justify-content: center;
    border-radius: 60px;
    font-size: 50px;
    font-weight: 600;
    line-height: 1;
    white-space: nowrap;
    color: var(--ink-light);
  }
  .promise--red    { background: var(--red); }
  .promise--orange { background: var(--orange); }
  .promise--yellow { background: var(--yellow); color: var(--ink-dark); }
  .promise--green  { background: var(--green); }
  .promise--blue   { background: var(--blue); }
  .promise--indigo { background: var(--indigo); }
  .promise--violet { background: var(--violet); }
</style>
</head>
<body>
  <main class="card">
    <p class="promise promise--red">I'll never leave you as long as you'll have me.</p>
    <p class="promise promise--orange">I'll never deny you my body.</p>
    <p class="promise promise--yellow">I'll never let you go to prison.</p>
    <p class="promise promise--green">I'll have a baby with you.</p>
    <p class="promise promise--blue">I'll marry you.</p>
    <p class="promise promise--indigo">I'll always love you.</p>
    <p class="promise promise--violet">I'll always stand by you and support you.</p>
  </main>
</body>
</html>
```